Harrowgate Construction And Masonry Ltd

Black background

Logo - attached

Services (bullet points)
New Builds
Extensions
Refurbishments
Alterations
Brickwork Specialists

Contact details - 01632 960418 or 0791 5530274

Email address - contact@harrowgateconstructionandmasonry.co.uk

Website - www.harrowgateconstructionandmasonry.co.uk

Facebook logo

```html
<!DOCTYPE html>
<html lang="en">
<head>
<meta charset="utf-8">
<title>Harrowgate Construction And Masonry Ltd – Brickwork Specialists Flyer</title>
<link rel="stylesheet" href="https://fonts.googleapis.com/css2?family=Roboto:ital,wght@0,300;0,400;0,500;0,700;1,900&display=swap">
<style>
  :root {
    --ink: #000000;
    --paper: #ffffff;
    --stage: #eceeed;
    --brand-green: #1ec864;
    --stripe-grey: #d9d9d9;
    --rule-grey: #5a5a5a;
    --muted: #cfcfcf;
    --photo-site-a: #8a7a6a;
    --photo-site-b: #c9c2b8;
    --photo-kitchen-a: #e6e4df;
    --photo-kitchen-b: #6b5040;
  }
  html, body {
    margin: 0;
    padding: 0;
    width: 1200px;
    height: 3537px;
    overflow: hidden;
    background: var(--stage);
  }
  .flyer {
    position: absolute;
    left: 0;
    top: 918px;
    width: 1200px;
    height: 1700px;
    display: block;
  }
  .brand-name { font-family: "Roboto", sans-serif; font-weight: 700; fill: var(--ink); }
  .headline { font-family: "Roboto", sans-serif; font-weight: 700; fill: var(--paper); }
  .subhead { font-family: "Roboto", sans-serif; font-weight: 300; fill: var(--paper); letter-spacing: 8px; }
  .service { font-family: "Roboto", sans-serif; font-weight: 500; fill: var(--paper); }
  .phone { font-family: "Roboto", sans-serif; font-weight: 900; font-style: italic; fill: var(--brand-green); letter-spacing: 2px; }
  .phone-or { font-family: "Roboto", sans-serif; font-weight: 900; font-style: italic; fill: var(--muted); }
  .contact-line { font-family: "Roboto", sans-serif; font-weight: 400; fill: var(--muted); }
  .social-handle { font-family: "Roboto", sans-serif; font-weight: 400; fill: #9a9a9a; }
</style>
</head>
<body>
<svg class="flyer" viewBox="0 0 874 1238" xmlns="http://www.w3.org/2000/svg" aria-label="Harrowgate Construction And Masonry Ltd brickwork specialists flyer">
  <defs>
    <linearGradient id="site-photo-tone" x1="0" y1="0" x2="1" y2="1">
      <stop offset="0" stop-color="var(--photo-site-b)"/>
      <stop offset="1" stop-color="var(--photo-site-a)"/>
    </linearGradient>
    <linearGradient id="kitchen-photo-tone" x1="0" y1="0" x2="0" y2="1">
      <stop offset="0" stop-color="var(--photo-kitchen-a)"/>
      <stop offset="0.6" stop-color="#b8b2a8"/>
      <stop offset="1" stop-color="var(--photo-kitchen-b)"/>
    </linearGradient>
  </defs>

  <!-- sheet -->
  <rect class="sheet" x="0" y="0" width="874" height="1238" fill="var(--paper)"/>

  <!-- dark panel -->
  <polygon class="dark-panel" points="0,430 838,430 838,540 874,562 874,1238 165,1238 0,622" fill="var(--ink)"/>

  <!-- lower-left light wedge with stripe -->
  <polygon class="corner-stripe" points="0,990 0,1100 40,1238 110,1238" fill="var(--stripe-grey)"/>

  <!-- site photo -->
  <rect class="photo-site" x="0" y="0" width="630" height="430" fill="url(#site-photo-tone)" role="img" aria-label="Rear of a brick house opened up during an extension build, with scaffolding, ladders and exposed brick piers"/>

  <!-- brand block -->
  <rect class="brand-mark" x="726" y="62" width="48" height="48" fill="var(--brand-green)"/>
  <text class="brand-name" x="750" y="160" font-size="36" text-anchor="middle">HARROWGATE</text>
  <text class="brand-name" x="750" y="184" font-size="11.5" text-anchor="middle">CONSTRUCTION AND MASONRY LTD</text>

  <!-- kitchen photo -->
  <rect class="photo-kitchen" x="145" y="258" width="693" height="465" fill="url(#kitchen-photo-tone)" role="img" aria-label="Finished open-plan kitchen extension with vaulted ceiling, roof lights, exposed brick chimney, island and herringbone floor"/>
  <rect class="photo-accent" x="145" y="256" width="693" height="4" fill="var(--brand-green)"/>

  <!-- headline -->
  <line class="rule" x1="383" y1="750" x2="874" y2="750" stroke="var(--rule-grey)" stroke-width="2"/>
  <text class="headline" x="228" y="841" font-size="99">BRICKWORK</text>
  <text class="subhead" x="226" y="897" font-size="48">SPECIALISTS</text>

  <!-- services -->
  <line class="service-lead" x1="0" y1="939" x2="230" y2="939" stroke="var(--brand-green)" stroke-width="3"/>
  <g class="service-bullets" fill="var(--brand-green)">
    <circle cx="230" cy="939" r="4.5"/>
    <circle cx="230" cy="975" r="4.5"/>
    <circle cx="230" cy="1011" r="4.5"/>
    <circle cx="230" cy="1048" r="4.5"/>
  </g>
  <text class="service" x="264" y="949" font-size="27">NEW BUILDS</text>
  <text class="service" x="264" y="985" font-size="27">EXTENSIONS</text>
  <text class="service" x="264" y="1021" font-size="27">REFURBISHMENTS</text>
  <text class="service" x="264" y="1058" font-size="27">ALTERATIONS</text>

  <!-- contact -->
  <line class="rule" x1="122" y1="1086" x2="874" y2="1086" stroke="var(--rule-grey)" stroke-width="2"/>
  <circle class="phone-icon-badge" cx="230" cy="1131" r="19" fill="#6e6e6e"/>
  <path class="phone-icon" d="M222,1122 c2,-2 4,-2 5,0 l3,5 c1,2 0,3 -2,4 c1,3 3,5 6,6 c1,-2 2,-3 4,-2 l5,3 c2,1 2,3 0,5 c-3,3 -7,3 -12,0 c-5,-3 -9,-7 -11,-12 c-1,-4 0,-7 2,-9 z" fill="var(--ink)"/>
  <text class="phone" x="264" y="1122" font-size="34">01632 960418</text>
  <line x1="292" y1="1133" x2="365" y2="1133" stroke="var(--muted)" stroke-width="1"/>
  <text class="phone-or" x="383" y="1138" font-size="14" text-anchor="middle">OR</text>
  <line x1="401" y1="1133" x2="436" y2="1133" stroke="var(--muted)" stroke-width="1"/>
  <text class="phone" x="264" y="1162" font-size="34">0791 5530274</text>
  <text class="contact-line" x="510" y="1121" font-size="15.5">www.harrowgateconstructionandmasonry.co.uk</text>
  <text class="contact-line" x="510" y="1146" font-size="15.5">contact@harrowgateconstructionandmasonry.co.uk</text>

  <!-- social -->
  <line class="rule" x1="150" y1="1176" x2="874" y2="1176" stroke="var(--rule-grey)" stroke-width="2"/>
  <circle class="social-badge" cx="230" cy="1207" r="18" fill="#6e6e6e"/>
  <text class="social-handle" x="263" y="1213" font-size="17">@Harrowgate-Construction-And-Masonry-Ltd</text>
</svg>
</body>
</html>
```